Adult Literacy Program - flyer to attract volunteers and students

We want a flyer that is engaging, colorful, modern and will appeal to our primary audience of adults aged 40-60. We are trying to attract both prospective volunteers (typically age 50+, mostly women) and students (typically aged 40+).
The flyer should feature diverse people working together in pairs of two, reading or talking, with a workbook or some reading material in front of them.

Our organization trains tutors to work one-on-one with adults who are learning how to read. Most of our adult students are non-native speakers of English. Many are of Haitian or Hispanic origin, so we would like some people who represent that demographic.

The Flyer should represent reading, learning, literacy, knowledge, growth,
and opportunities.
Our students are learning to read so they can advance their job opportunities.

Target Market(s)

Adults aged 40-60, primarily women, retired, volunteers

Industry/Entity Type

Education

Font styles to use
Serif
Sans Serif

Colors

Designer to choose colors to be used in the design.

Requirements
Must have
• - UPDATE: Should be designed as a TRI-FOLD brochure on 8.5 x 11 inch paper that will be folded into thirds.
• - Images of diverse people, women and men, who look Hispanic, Haitian and other nationalities as well as Caucasian.
• - Our logo on the front cover
Nice to have
• The sample flyer is very boring and dry! We are open to different ways of presenting the text.

```html
<!DOCTYPE html>
<html lang="en">
<head>
<meta charset="utf-8">
<title>Volunteer – Adult Literacy Tri-fold</title>
<link href="https://fonts.googleapis.com/css2?family=Arimo:wght@400;700&family=Libre+Baskerville:wght@700&family=Dancing+Script:wght@400&display=swap" rel="stylesheet">
<style>
  :root {
    --navy: #1f2a5a;
    --ink: #1a1a1a;
    --sky: #a6dcf1;
    --sky-mid: #5cc3e6;
    --cyan: #10a9dc;
    --band-light: #56c1e6;
    --white: #ffffff;
    --page: #e9e9e9;
    --maroon: #7a1f1f;
  }
  * { box-sizing: border-box; margin: 0; padding: 0; }
  html, body { width: 1200px; height: 1200px; overflow: hidden; background: var(--page); }
  body { position: relative; font-family: "Arimo", Arial, sans-serif; color: var(--ink); }

  .brochure {
    position: absolute; left: 20px; top: 154px;
    width: 1300px; height: 1000px;
    transform: scale(0.8923); transform-origin: top left;
    background: var(--white);
    box-shadow: 0 4px 14px rgba(0,0,0,.25);
  }
  .inside-panel { position: absolute; left: 0; top: 0; width: 866px; height: 1000px; background: var(--white); }
  .cover-panel  { position: absolute; left: 866px; top: 0; width: 434px; height: 1000px; background: var(--sky); overflow: hidden; }

  .hero { position: absolute; left: 0; top: 0; width: 866px; height: 460px; display: block; }

  .students { position: absolute; left: 15px; top: 436px; width: 460px; }
  .students h2 { font-size: 25px; font-weight: 700; margin-bottom: 12px; }
  .students .intro { font-size: 19.5px; margin-bottom: 8px; }
  .students ul { list-style: none; }
  .students li { position: relative; font-size: 19.5px; line-height: 37px; }
  .students li::before { content: ""; position: absolute; width: 6px; height: 6px; border-radius: 50%; background: var(--ink); top: 16px; }
  .needs li { padding-left: 59px; }
  .needs li::before { left: 38px; }
  .facts li { padding-left: 35px; }
  .facts li::before { left: 3px; }

  .motto { position: absolute; left: 72px; top: 780px; font-family: "Dancing Script", cursive; font-size: 52px; line-height: 58px; color: var(--navy); transform: rotate(-3deg); }
  .motto span { display: block; padding-left: 12px; }

  .contact { position: absolute; left: 450px; top: 470px; width: 400px; text-align: center; }
  .contact p { font-size: 19.5px; line-height: 24px; }
  .contact .lead { font-weight: 700; margin-bottom: 13px; }
  .contact .label { font-weight: 700; margin-top: 13px; }
  .contact .phone { font-size: 29px; line-height: 36px; }
  .contact .email { margin-top: 12px; }
  .contact .email b { font-weight: 700; }

  .library-name { position: absolute; left: 500px; top: 820px; width: 300px; text-align: center; font-weight: 700; font-size: 24px; line-height: 29px; color: var(--navy); }
  .library-project { position: absolute; left: 500px; top: 903px; width: 300px; text-align: center; font-weight: 700; font-size: 20px; color: var(--maroon); }

  .footer-rule { position: absolute; left: 0; top: 940px; width: 866px; height: 6px; background: var(--navy); }
  .footer-bar { position: absolute; left: 0; top: 952px; width: 866px; height: 48px; background: var(--cyan); }
  .footer-bar p { position: absolute; top: 10px; font-size: 23px; font-weight: 700; color: var(--navy); }
  .footer-bar .web { left: 50px; }
  .footer-bar .call { left: 497px; }

  .cover-title { position: absolute; left: 0; top: 18px; width: 434px; text-align: center; font-family: "Libre Baskerville", Georgia, serif; font-weight: 700; font-size: 58px; color: var(--ink); }
  .cover-sub { position: absolute; left: 0; top: 86px; width: 434px; text-align: center; font-family: "Dancing Script", cursive; font-size: 44px; color: var(--ink); }
  .cover-art { position: absolute; left: 0; top: 150px; width: 434px; height: 620px; display: block; }
  .cover-base { position: absolute; left: 0; top: 760px; width: 434px; height: 240px; background: var(--sky-mid); }

  .program-badge { position: absolute; left: 155px; top: 638px; width: 270px; height: 270px; border-radius: 50%; background: var(--white); display: flex; align-items: center; justify-content: center; text-align: center; }
  .program-badge p { font-weight: 700; font-size: 30px; line-height: 36px; color: var(--cyan); }

  .cover-call { position: absolute; left: 56px; top: 918px; font-size: 25px; font-weight: 700; line-height: 27px; color: var(--navy); }
  .cover-call span { display: block; padding-left: 63px; }
</style>
</head>
<body>
<div class="brochure">

  <section class="inside-panel">
    <svg class="hero" viewBox="0 0 866 460" preserveAspectRatio="none">
      <defs>
        <linearGradient id="groupTone" x1="0" y1="0" x2="1" y2="1">
          <stop offset="0" stop-color="#8a3a3f"/>
          <stop offset=".45" stop-color="#c9a58d"/>
          <stop offset="1" stop-color="#9bb7d8"/>
        </linearGradient>
      </defs>
      <path role="img" aria-label="Photo: a diverse group of adult tutors and learners smiling around a library table with books" d="M0 0H866V310C650 410 320 420 0 348Z" fill="url(#groupTone)"/>
      <path d="M0 348C320 420 650 410 866 310V332C650 438 320 446 0 368Z" fill="var(--band-light)"/>
      <path d="M0 368C320 446 650 438 866 332V352C640 470 300 476 0 382Z" fill="var(--navy)"/>
    </svg>

    <div class="students">
      <h2>Students</h2>
      <p class="intro">Students are adults in need of</p>
      <ul class="needs">
        <li>basic literacy skills</li>
        <li>pre-GED skills</li>
        <li>conversational English</li>
      </ul>
      <ul class="facts">
        <li>Tutoring is free of charge</li>
        <li>Tutoring is one-on-one</li>
        <li>Flexible scheduling during library hours</li>
        <li>Lessons focus on student goals.</li>
      </ul>
    </div>

    <p class="motto">If you can read,<span>you can tutor!</span></p>

    <div class="contact">
      <p class="lead">Don’t waste a moment!</p>
      <p>Contact us today to learn more.</p>
      <p class="label">Volunteer Desk :</p>
      <p class="phone">555-014-2270</p>
      <p class="label">Lakeview, Cedar Point &amp; Millbrook</p>
      <p class="phone">555-013-8841</p>
      <p class="email"><b>email</b> : literacy@harborlibrary.org</p>
    </div>

    <p class="library-name">Harbor County<br>Library System</p>
    <p class="library-project">Adult Literacy Project</p>

    <div class="footer-rule"></div>
    <div class="footer-bar">
      <p class="web">log on : www.harborlibrary.org</p>
      <p class="call">contact us 555-014-2270</p>
    </div>
  </section>

  <section class="cover-panel">
    <h1 class="cover-title">Volunteer</h1>
    <p class="cover-sub">Enrich a Life!</p>

    <svg class="cover-art" viewBox="0 0 434 620" preserveAspectRatio="none">
      <defs>
        <linearGradient id="pairTone" x1="0" y1="0" x2="1" y2="1">
          <stop offset="0" stop-color="#6a4a3a"/>
          <stop offset=".5" stop-color="#9db8d6"/>
          <stop offset="1" stop-color="#d9d4cc"/>
        </linearGradient>
      </defs>
      <path d="M0 12C140 -6 300 -4 434 48V620H0Z" fill="var(--navy)"/>
      <path d="M0 22C140 6 300 8 434 60V80C300 30 140 26 0 40Z" fill="#7fb0dc"/>
      <path role="img" aria-label="Photo: an adult learner reading a workbook with a tutor in a library" d="M0 40C140 26 300 30 434 80V520C330 560 200 600 0 610Z" fill="url(#pairTone)"/>
      <path d="M434 520C330 560 200 600 0 610V620H434Z" fill="var(--sky-mid)"/>
    </svg>
    <div class="cover-base"></div>

    <div class="program-badge"><p>OPEN PAGE<br>READERS</p></div>

    <p class="cover-call">Help an adult to read<span>write or speak English</span></p>
  </section>

</div>
</body>
</html>
```